Letterhead - Quarrington Law Group

I receive a fantastic logo from you guys and I'd like to incorporate it into business cards and letterhead. I accidentally approved design No. 32361474 and contacted designer Ravindra, and Ravindra sent me the zip folder for Design No. 32361417, which I very much appreciate.
I'd like to order business cards and letterhead with Design No. 32361417 as soon as possible, but I want to make sure that you incorporate the correct design (attached). I'd also like to provide my information to add (address, phone number, email, fax) but I'm not quite sure how to do it.
The information that I would like on the business cards and letterhead is as follows:
Quarrington Law Group
Theodore K. Quarrington, Esq.
2741 Hollis Avenue, Suite 520
San Francisco, CA 94087
Office: (415) 378-6130
Fax: (415) 746-0183
ted@quarringtonlawgroup-example.com
Thanks in advance for any guidance.
Ted Quarrington
Quarrington Law Group
(415) 831-4497 (cell)

```html
<!DOCTYPE html>
<html lang="en">
<head>
<meta charset="utf-8">
<title>Quarrington Law Group – Letterhead</title>
<link rel="stylesheet" href="https://fonts.googleapis.com/css2?family=Source+Sans+3:wght@400;600;700&display=swap">
<style>
  :root{
    --brand-blue:#178dc9;
    --ink:#111214;
    --body-grey:#7d7f82;
    --band-grey:#d1d3d4;
    --band-light:#e6e7e8;
    --night:#060709;
    --paper:#ffffff;
    --backdrop:#ececed;
  }
  *{box-sizing:border-box;margin:0;padding:0}
  html,body{width:1189px;height:1200px;overflow:hidden;background:var(--backdrop)}
  body{font-family:"Source Sans 3",sans-serif;color:var(--ink);position:relative}
  .letterhead{position:absolute;left:205px;top:99px;width:779px;height:1001px;background:var(--paper);overflow:hidden}
  .letterhead__waves{position:absolute;inset:0;width:100%;height:100%}
  .brand-name{position:absolute;right:33px;top:72px;color:var(--paper);font-weight:600;font-size:19px;letter-spacing:.3px;white-space:nowrap}
  .recipient{position:absolute;left:34px;top:186px;line-height:1}
  .label{font-size:15.5px;display:block}
  .person-name{color:var(--brand-blue);font-weight:700;font-size:20px;display:block;margin-top:5px}
  .role{font-size:15.5px;display:block;margin-top:4px}
  .contact-lines{list-style:none;margin-top:8px;font-size:12.5px}
  .contact-lines li{height:20px;line-height:20px}
  .contact-lines b{color:var(--brand-blue);font-weight:700}
  .letter-date{position:absolute;left:539px;top:281px;font-size:12.5px}
  .letter-date span{color:var(--brand-blue)}
  .salutation{position:absolute;left:34px;top:343px;font-size:19px;font-weight:700}
  .letter-body{position:absolute;left:34px;top:383px;width:712px;color:var(--body-grey);font-size:15px;line-height:22.3px}
  .letter-body p{text-align:justify;text-align-last:left}
  .sender{position:absolute;left:33px;top:691px;line-height:1}
  .signature-mark{display:block;width:122px;height:22px;margin-top:10px;background:#eef0f1;border-radius:3px}
  .signature-rule{width:122px;height:1.5px;background:var(--brand-blue);margin-top:3px}
  .signature-label{display:block;font-size:15.5px;margin-top:7px}
  .footer-contacts{position:absolute;right:33px;top:875px;list-style:none;color:var(--paper);font-size:13.5px;text-align:right}
  .footer-contacts li{display:flex;justify-content:flex-end;align-items:center;height:19.4px;gap:6px}
  .footer-contacts svg{width:14px;height:14px;flex:none}
</style>
</head>
<body>
<main class="letterhead">
  <svg class="letterhead__waves" viewBox="0 0 1039 1335" preserveAspectRatio="none" aria-hidden="true">
    <rect width="1039" height="1335" fill="var(--night)"/>
    <path d="M0,143 C300,30 650,-25 1039,55 L1039,700 L0,700Z" fill="var(--brand-blue)"/>
    <path d="M0,150 C200,80 380,60 480,60 C700,62 930,230 1039,423 L1039,700 L0,700Z" fill="var(--band-grey)"/>
    <path d="M0,200 C220,120 420,92 520,92 C740,98 950,250 1039,423 L1039,700 L0,700Z" fill="var(--band-light)"/>
    <path d="M0,230 C200,170 360,150 460,150 C720,150 960,280 1039,423 L1039,1335 L0,1335Z" fill="var(--paper)"/>
    <path d="M0,1102 C300,1190 540,1190 740,1135 C900,1085 1010,990 1039,870 L1039,1335 L0,1335Z" fill="var(--band-light)"/>
    <path d="M0,1140 C260,1225 500,1240 680,1215 C880,1170 1010,1030 1039,890 L1039,1335 L0,1335Z" fill="var(--band-grey)"/>
    <path d="M0,1190 C200,1260 420,1270 600,1228 C790,1180 950,1060 1039,912 L1039,1335 L0,1335Z" fill="var(--brand-blue)"/>
    <path d="M0,1200 C350,1330 750,1355 1039,1305 L1039,1335 L0,1335Z" fill="var(--night)"/>
  </svg>

  <div class="brand-name">Quarrington Law Group</div>

  <section class="recipient">
    <span class="label">TO</span>
    <span class="person-name">Theodore K. Quarrington</span>
    <span class="role">Managing Director</span>
    <ul class="contact-lines">
      <li><b>P:</b> (415) 378-6130</li>
      <li><b>F:</b> (415) 746-0183</li>
      <li><b>A:</b> 2741 Hollis Avenue,Suite 520</li>
      <li>San Francisco, CA 94087</li>
    </ul>
  </section>

  <div class="letter-date"><span>Date</span> : 1/3/2024</div>

  <h1 class="salutation">Dear Sir</h1>

  <article class="letter-body">
    <p>Lorem ipsum dolor sit amet, consectetuer adipiscing elit, sed diam nonummy nibh euismod tincidunt ut laoreet dolore magna aliquam erat volutpat. Ut wisi enim ad minim veniam, quis nostrud exerci tation ullamcorper suscipit lobortis nisl ut aliquip</p>
    <p>ex ea commodo consequat. Duis autem vel eum iriure dolor in hendrerit in vulputate velit esse molestie consequat, vel illum dolore eu feugiat nulla facilisis at vero eros et accumsan et iusto odio dignissim qui blandit praesent luptatum zzril delenit augue duis dolore te feugait nulla facilisi.Lorem ipsum dolor sit amet, cons ectetuer adipiscing elit, sed diam nonummy nibh euismod tincidunt ut laoreet dolore magna a</p>
    <p>nisl ut aliquip ex ea commodo consequat.Lorem ipsum dolor sit amet, consectetuer adipiscing elit, sed diam nonum-my nibh euismod tincidunt ut laoreet dolore magna aliquam erat volutpat. Ut wisi enim ad minim veniam, quis nostrud exerci tation ullamcorper suscipit lobortis nisl ut aliquip ex ea commodo consequat. Duis autem vel eum iriure dolor in hendrerit in vulputate velit esse molestie consequat, vel illum dolore eu feugiat nulla facilisis at vero eros et accumsan et iusto odio dignissim qui blandit praesent luptatum zzril delenit augue duis dolore te feugait nulla facilisi.</p>
  </article>

  <section class="sender">
    <span class="label">From</span>
    <span class="person-name">Ted Quarrington</span>
    <span class="role">Owner</span>
    <span class="signature-mark" role="img" aria-label="Handwritten signature of Ted Quarrington"></span>
    <div class="signature-rule"></div>
    <span class="signature-label">Signature</span>
  </section>

  <ul class="footer-contacts">
    <li>(415) 831-4497
      <svg viewBox="0 0 14 14"><circle cx="7" cy="7" r="7" fill="#fff"/><path d="M4.3,3.5 l1.4,-.3 .8,1.8 -.9,.7 c.4,1 1.1,1.7 2.1,2.1 l.7,-.9 1.8,.8 -.3,1.4 C6.6,9.3 4.6,7.3 4.3,3.5Z" fill="var(--brand-blue)"/></svg></li>
    <li>(415) 378-6130
      <svg viewBox="0 0 14 14"><circle cx="7" cy="7" r="7" fill="#fff"/><path d="M3.5,6 q3.5,-3 7,0 l-.8,1 -1.2,-.6 v-.9 q-1.5,-.5 -3,0 v.9 l-1.2,.6Z M4.5,8 h5 v2 h-5Z" fill="var(--brand-blue)"/></svg></li>
    <li>(415) 746-0183
      <svg viewBox="0 0 14 14"><circle cx="7" cy="7" r="7" fill="#fff"/><path d="M4.8,3.5 h4.4 v2 h-4.4Z M3.5,6 h7 v3 h-1.3 v1.5 h-4.4 v-1.5 h-1.3Z" fill="var(--brand-blue)"/></svg></li>
    <li>ted@quarringtonlawgroup-example.com
      <svg viewBox="0 0 14 14"><circle cx="7" cy="7" r="7" fill="#fff"/><rect x="3.5" y="4.5" width="7" height="5" fill="var(--brand-blue)"/><path d="M3.7,4.7 7,7.3 10.3,4.7" stroke="#fff" stroke-width=".8" fill="none"/></svg></li>
    <li>2741 Hollis Avenue,Suite 520 San Francisco, CA 94087
      <svg viewBox="0 0 14 14"><circle cx="7" cy="7" r="7" fill="#fff"/><path d="M7,11 C5,8.5 4.3,7.3 4.3,5.9 a2.7,2.7 0 0 1 5.4,0 C9.7,7.3 9,8.5 7,11Z" fill="var(--brand-blue)"/><circle cx="7" cy="5.9" r="1" fill="#fff"/></svg></li>
  </ul>
</main>
</body>
</html>
```